No Credit Score TQ and KSV

I'm looking for a banner to display on emails as well as facebook. The facebook banner would need to be square and the other size is 728 x 90. We are a mortgage company that does mostly Military home loans. We would like to start out with just this banner, then do about 20 others once we find the right designer. I need something simple but that stands out. Our company website is www.harborpeakloans.com. The text for this will be ( Ask about our "No Credit Score" program for KSV and TQ)

```html
<!DOCTYPE html>
<html lang="en">
<head>
<meta charset="utf-8">
<title>No Credit Score Banner Set</title>
<link rel="stylesheet" href="https://fonts.googleapis.com/css2?family=Oswald:wght@300;400;500&family=Lato:wght@400&display=swap">
<style>
:root{
  --page:#e8e9ea;
  --label:#8a8b8d;
  --slate:#4d4d4f;
  --green:#79a13b;
  --white:#ffffff;
  --photo-a:#8a7b70;
  --photo-b:#b07a86;
  --photo-c:#7a8068;
}
*{margin:0;padding:0;box-sizing:border-box}
html,body{width:1200px;height:837px;overflow:hidden;background:var(--page)}
body{position:relative;font-family:"Oswald",sans-serif;color:var(--white)}
.size-label{position:absolute;font:400 11px/1 "Oswald",sans-serif;color:var(--label);letter-spacing:.3px}
.banner{position:absolute;background:var(--slate);overflow:hidden;box-shadow:2px 3px 5px rgba(0,0,0,.28)}
.banner svg.shapes{position:absolute;inset:0}
.brand{position:absolute;display:flex;align-items:center;justify-content:center;gap:6px;transform:translateX(-50%);font-weight:300;color:var(--white);white-space:nowrap;letter-spacing:1px}
.brand .dot{width:.55em;height:.55em;border-radius:50%;background:var(--white)}
.copy{position:absolute;transform:translateX(-50%);text-align:center;white-space:nowrap;font-weight:300;line-height:1}
.copy .ask,.copy .program{display:block;text-transform:uppercase}
.copy .offer{display:block;color:var(--green);text-transform:uppercase}
.divider{position:absolute;height:1px;transform:translateX(-50%);background:linear-gradient(90deg,transparent,#2f2f30,transparent)}
.cta{position:absolute;display:flex;align-items:center;justify-content:center;background:var(--green);color:var(--white);font-weight:500;letter-spacing:1px;text-transform:uppercase;box-shadow:1px 2px 3px rgba(0,0,0,.3)}
.url{position:absolute;transform:translateX(-50%);font-family:"Lato",sans-serif;white-space:nowrap;color:var(--white)}
.vrule{position:absolute;width:1px;background:#3c3c3d}
</style>
</head>
<body>

<span class="size-label" style="left:78px;top:60px">160 X 600</span>
<span class="size-label" style="left:309px;top:292px">300 X 250</span>
<span class="size-label" style="left:697px;top:263px">336 X 280</span>
<span class="size-label" style="left:309px;top:638px">728 X 90</span>

<!-- Skyscraper 160 x 600 -->
<section class="banner banner-skyscraper" style="left:78px;top:87px;width:180px;height:674px">
  <svg class="shapes" width="180" height="674" viewBox="0 0 180 674">
    <defs><linearGradient id="photoSky" x1="0" y1="0" x2="1" y2="1"><stop offset="0" stop-color="var(--photo-a)"/><stop offset=".6" stop-color="var(--photo-b)"/><stop offset="1" stop-color="var(--photo-c)"/></linearGradient></defs>
    <polygon points="0,0 180,0 180,171 0,256" fill="url(#photoSky)" role="img" aria-label="Photo of a smiling military family: soldier in camouflage, mother and toddler in front of a home"/>
    <polygon points="105,0 180,0 180,77" fill="var(--green)"/>
    <polygon points="0,588 180,645 180,674 0,674" fill="var(--green)"/>
  </svg>
  <div class="brand" style="left:90px;top:322px;font-size:16px"><span class="dot"></span>HARBOR PEAK</div>
  <div class="copy" style="left:90px;top:420px">
    <span class="ask" style="font-size:14px">Ask about our</span>
    <span class="offer" style="font-size:22px;margin:2px 0">"No Credit Score"</span>
    <span class="program" style="font-size:14px">Program for KSV and TQ</span>
  </div>
  <div class="divider" style="left:90px;top:497px;width:120px"></div>
  <div class="cta" style="left:18px;top:512px;width:145px;height:33px;font-size:15px">Get Started</div>
  <div class="url" style="left:90px;top:553px;font-size:10.5px">www.harborpeakloans.com</div>
</section>

<!-- Medium rectangle 300 x 250 -->
<section class="banner banner-medium" style="left:309px;top:322px;width:338px;height:281px">
  <svg class="shapes" width="338" height="281" viewBox="0 0 338 281">
    <defs><linearGradient id="photoMed" x1="0" y1="0" x2="1" y2="1"><stop offset="0" stop-color="var(--photo-a)"/><stop offset=".55" stop-color="var(--photo-b)"/><stop offset="1" stop-color="var(--photo-c)"/></linearGradient></defs>
    <polygon points="0,0 209,0 112,281 0,281" fill="url(#photoMed)" role="img" aria-label="Photo of a smiling military family: mother, toddler and soldier in camouflage"/>
    <polygon points="0,180 125,281 0,281" fill="var(--green)"/>
    <polygon points="265,0 338,0 338,74" fill="var(--green)"/>
  </svg>
  <div class="brand" style="left:249px;top:48px;font-size:14px"><span class="dot"></span>HARBOR PEAK</div>
  <div class="copy" style="left:249px;top:119px">
    <span class="ask" style="font-size:14px">Ask about our</span>
    <span class="offer" style="font-size:22px;margin:2px 0">"No Credit Score"</span>
    <span class="program" style="font-size:14px">Program for KSV and TQ</span>
  </div>
  <div class="divider" style="left:249px;top:195px;width:120px"></div>
  <div class="cta" style="left:176px;top:210px;width:145px;height:33px;font-size:15px">Get Started</div>
  <div class="url" style="left:249px;top:251px;font-size:10.5px">www.harborpeakloans.com</div>
</section>

<!-- Large rectangle 336 x 280 -->
<section class="banner banner-large" style="left:697px;top:288px;width:379px;height:316px">
  <svg class="shapes" width="379" height="316" viewBox="0 0 379 316">
    <defs><linearGradient id="photoLg" x1="0" y1="0" x2="1" y2="1"><stop offset="0" stop-color="var(--photo-a)"/><stop offset=".55" stop-color="var(--photo-b)"/><stop offset="1" stop-color="var(--photo-c)"/></linearGradient></defs>
    <polygon points="0,0 233,0 124,316 0,316" fill="url(#photoLg)" role="img" aria-label="Photo of a smiling military family: mother, toddler and soldier in camouflage"/>
    <polygon points="0,181 142,316 0,316" fill="var(--green)"/>
    <polygon points="299,0 379,0 379,80" fill="var(--green)"/>
  </svg>
  <div class="brand" style="left:277px;top:60px;font-size:16px"><span class="dot"></span>HARBOR PEAK</div>
  <div class="copy" style="left:277px;top:133px">
    <span class="ask" style="font-size:16px">Ask about our</span>
    <span class="offer" style="font-size:25px;margin:3px 0">"No Credit Score"</span>
    <span class="program" style="font-size:16px">Program for KSV and TQ</span>
  </div>
  <div class="divider" style="left:277px;top:219px;width:130px"></div>
  <div class="cta" style="left:198px;top:236px;width:163px;height:36px;font-size:16px">Get Started</div>
  <div class="url" style="left:279px;top:281px;font-size:12px">www.harborpeakloans.com</div>
</section>

<!-- Leaderboard 728 x 90 -->
<section class="banner banner-leaderboard" style="left:309px;top:660px;width:818px;height:102px">
  <svg class="shapes" width="818" height="102" viewBox="0 0 818 102">
    <defs><linearGradient id="photoLb" x1="0" y1="0" x2="1" y2="1"><stop offset="0" stop-color="var(--photo-a)"/><stop offset=".5" stop-color="var(--photo-b)"/><stop offset="1" stop-color="var(--photo-c)"/></linearGradient></defs>
    <polygon points="0,0 261,0 193,102 0,102" fill="url(#photoLb)" role="img" aria-label="Photo of a smiling military family: mother, toddler and soldier in front of a home"/>
    <polygon points="215,0 261,0 240,26" fill="var(--green)"/>
    <polygon points="739,102 818,0 818,102" fill="var(--green)"/>
  </svg>
  <div class="brand" style="left:292px;top:42px;font-size:13px"><span class="dot"></span>HARBOR PEAK</div>
  <div class="copy" style="left:446px;top:14px">
    <span class="ask" style="font-size:19px">Ask about our</span>
    <span class="offer" style="font-size:29px;margin:2px 0">"No Credit Score"</span>
    <span class="program" style="font-size:19px">Program for KSV and TQ</span>
  </div>
  <div class="vrule" style="left:574px;top:0;height:102px"></div>
  <div class="cta" style="left:584px;top:27px;width:167px;height:37px;font-size:17px">Get Started</div>
  <div class="url" style="left:667px;top:74px;font-size:12px">www.harborpeakloans.com</div>
</section>

</body>
</html>
```